Consultative Employee Benifits Firm Needs Business Card Design Project

We need a business card design for a new company based in Northern Virginia called "Telman Financial Services, LLC. We are both a wealth management advisory firm, as well as an employee benefits firm, which strives to provide superior creativity in employee benefits plan design and greater client and employee satisfaction. We are obsessed with service and follow up.

Our firm specializes in the areas of group health, life, dental, disability, voluntary benefits, Executive Benefits, HRA and HSA programs. We offer competitive employee benefit packages and pricing models for single or multi-state/multi location companies by maintaining preferred relationships with a large number of regional and national carriers.

Our firm also considers the many dimensions of your wealth through an integrated process we call wealth structuring — a comprehensive, dynamic approach to building, preserving, enjoying and transferring your wealth. And because we are often dealing with complex ownership structures and complicated, changing family dynamics, we bring the highest level of experience and creativity to managing your wealth. We work hard to help ensure that your legacy lasts by preparing your children for the financial challenges and opportunities that are headed their way.

Our final design should communicate an integrated approach to finanial safety and optimization
Updates

 Due to a few designers not accepting due to low budget, I have increased budget payout 19%. 

Project Deadline Extended
Reason: I have only heard from 12 designers. So, maybe I did not give the right amount of time to do the project. For the designers that have submitted their designs, thank you. I have seen three or four designs that I liked and might end up with one of them after it's all over, but I thought I would see between 20 - 25 before everything was over. Dan

Target Market(s)

Professionals; doctors, contractors, small to mid size business owners, ages 50 -65 with nert worth of 2MM

Industry/Entity Type

Financial

Requirements
Must have
• Telman Financial Services, LLC

Dan Telman
President
41957 Marwick Hollow Street
Quenford Glen, 20871

Office: 703 555-0184
Cell: 703 555-0127
Fax: 703 555-0163
Email: dantelman@quorvex.net
Should not have
• No pink or yellow colors.
No generic clipart (coins, dollar signs, money bags, graphs)

```html
<!DOCTYPE html>
<html lang="en">
<head>
<meta charset="utf-8">
<title>Telman Financial Services, LLC — Card Back</title>
<link rel="stylesheet" href="https://fonts.googleapis.com/css2?family=Questrial&display=swap">
<style>
  :root {
    --card-bg: #262626;
    --mark-grey: #8c8c8c;
    --text-grey: #a8a8a8;
  }
  * { margin: 0; padding: 0; box-sizing: border-box; }
  html, body {
    width: 1200px;
    height: 600px;
    overflow: hidden;
    background: var(--card-bg);
  }
  .card {
    position: relative;
    width: 1200px;
    height: 600px;
    background: var(--card-bg);
    font-family: "Questrial", "Century Gothic", sans-serif;
    color: var(--text-grey);
  }
  .brand {
    position: absolute;
    left: 0;
    right: 0;
    top: 150px;
    text-align: center;
  }
  .brand-mark {
    display: block;
    font-size: 150px;
    line-height: 170px;
    font-weight: 400;
    letter-spacing: -2px;
    color: var(--mark-grey);
  }
  .brand-name {
    display: block;
    margin-top: 8px;
    font-size: 23px;
    letter-spacing: 0.3px;
    color: var(--text-grey);
  }
  .address {
    position: absolute;
    left: 0;
    right: 0;
    bottom: 12px;
    text-align: center;
    padding-left: 24px;
    font-style: normal;
    color: var(--text-grey);
  }
  .address-street {
    display: block;
    font-size: 23px;
    line-height: 30px;
  }
  .address-city {
    display: block;
    font-size: 28px;
    line-height: 36px;
  }
</style>
</head>
<body>
  <main class="card">
    <div class="brand">
      <span class="brand-mark">tfs</span>
      <span class="brand-name">Telman Financial Services, LLC.</span>
    </div>
    <address class="address">
      <span class="address-street">41957 Marwick Hollow Street</span>
      <span class="address-city">Quenford Glen, 20871</span>
    </address>
  </main>
</body>
</html>
```